New Word Template Design Project

Dellvane needs a modern and fresh corporate word template (*.dotm). We are a technology integrator the operates in the ICT sector in Portugal and Spain. Our solutions and services are detailed here: dellvane-example.com.
This word template should have mainly Dellvane's blue tones, and among other purposes, it's meant to be the basis of our commercial proposals. As such, in the cover page we need to place info such as: project name, client name, Dellvane reference, client reference, date and document type (the latter with less visual emphasis).
Our official font is Raleway and we are also sending our Brand Manual where the official company colors are specified.
Concerning the components of the document, we would like to have an index, 5 headings levels, 5 bullet points levels, 2 table styles and the other components that are part of the document we are also sending.

Target Market(s)

Executives and IT Directors

Industry/Entity Type

Information Technology

Font styles to use
Other font styles liked:
• Raleway

Colors
249fd3

Requirements
Must have
• Not jeopardizing the designers creativity, we would like it to be aligned with our website image.
• Respect brand colors (mostly the blue ones) and font
• Cover page info: project name, client name, Dellvane reference, client reference, date and document type
• 5 levels of headings considering a report
• 5 levels of bullet points
• 2 layouts for tables
• index
Nice to have
• A professional corporate template, yet conveying some modern, dynamic and "fresh" image.
Should not have
• Too many colors
• An unprofessional image

```html
<!DOCTYPE html>
<html lang="pt">
<head>
<meta charset="utf-8">
<title>Dellvane – Modelo de Proposta</title>
<link href="https://fonts.googleapis.com/css2?family=Raleway:wght@400;500;600;700&family=Oswald:wght@500;600&display=swap" rel="stylesheet">
<style>
:root{
  --stage:#414141;
  --brand:#249fd3;
  --brand-deep:#1a8ccc;
  --navy:#0d1f3c;
  --ink:#222;
  --rule:#8aa3c2;
  --paper:#fff;
}
*{margin:0;padding:0;box-sizing:border-box}
html,body{width:1200px;height:1200px;overflow:hidden;background:var(--stage);font-family:"Raleway",sans-serif;color:var(--ink)}
.page{position:absolute;background:var(--paper);overflow:hidden}
.p-cover{left:47px;top:189px;width:290px;height:407px}
.p-toc{left:441px;top:189px;width:294px;height:411px}
.p-summary{left:823px;top:189px;width:296px;height:415px}
.p-scope{left:230px;top:644px;width:290px;height:406px}
.p-method{left:699px;top:644px;width:290px;height:406px}

.wordmark{display:flex;align-items:center;gap:5px;color:var(--brand);font-weight:500}
.wordmark .dot{width:8px;height:8px;border-radius:50%;background:var(--brand)}
.footer{position:absolute;left:0;right:0;bottom:0;height:13px;background:var(--navy);color:#cfe3f5;font-size:5px;display:flex;justify-content:space-between;align-items:center;padding:0 12px}

/* cover */
.cover-logo{position:absolute;top:0;height:75px;width:100%;display:flex;justify-content:center;align-items:center}
.cover-logo .wordmark{font-size:20px}
.cover-logo .dot{width:14px;height:14px}
.cover-photo{position:absolute;top:75px;height:199px;width:100%;background:radial-gradient(ellipse at 60% 35%,#e47aa8 0%,#7a3e9a 30%,transparent 55%),linear-gradient(160deg,#2a1550 0%,#1b3f8c 50%,#0a6fb8 75%,#06183a 100%)}
.cover-title{position:absolute;top:280px;width:100%;text-align:center;font-family:"Oswald",sans-serif;font-weight:600;font-size:29px;color:var(--brand-deep);letter-spacing:.5px}
.cover-client{position:absolute;top:322px;width:100%;text-align:center;font-family:"Oswald",sans-serif;font-size:11px;color:var(--brand-deep)}
.cover-date{position:absolute;top:338px;left:50%;transform:translateX(-50%);background:var(--navy);color:#fff;font-family:"Oswald",sans-serif;font-size:10.5px;line-height:14px;padding:0 6px;border-radius:8px;white-space:nowrap}
.cover-ref{position:absolute;top:355px;width:100%;text-align:center;font-size:11px;color:#333}
.cover-band{position:absolute;left:0;right:0;bottom:0;height:30px;background:var(--brand);border-top:3px solid var(--navy);color:#fff;font-size:8px;display:flex;justify-content:center;align-items:center}

/* toc */
.toc-logo{position:absolute;top:0;height:60px;width:100%;display:flex;justify-content:center;align-items:center}
.toc-logo .wordmark{font-size:16px}
.toc-logo .dot{width:12px;height:12px}
.blue-rule{position:absolute;left:0;right:0;height:3px;background:var(--brand)}
.toc-bg{position:absolute;top:63px;bottom:13px;left:0;right:0;background:linear-gradient(120deg,#fff 40%,#eef3f8 70%,#f7f9fb)}
.toc-title{position:absolute;top:66px;left:24px;font-size:11px;font-weight:500;color:var(--brand)}
.toc-list{position:absolute;top:82px;left:28px;right:18px;list-style:none}
.toc-list li{display:flex;align-items:flex-end;height:8.65px;font-size:3.8px;color:#666}
.toc-list li.lvl1{font-weight:700;color:#222}
.toc-list li span.leader{flex:1;border-bottom:.5px solid var(--rule);margin:0 6px 1.5px}

/* inner header */
.inner-head{position:absolute;top:0;left:0;right:0;height:38px}
.inner-head .wordmark{position:absolute;left:13px;top:14px;font-size:8px}
.inner-head .dot{width:6px;height:6px}
.inner-head address{position:absolute;right:9px;top:12px;font-style:normal;font-size:3.3px;line-height:1.45;color:#333}
.p-summary .blue-rule,.p-scope .blue-rule,.p-method .blue-rule{top:38px}

/* summary */
.sum-body{position:absolute;top:48px;left:18px;right:28px;font-size:5px;line-height:1.35}
.sum-body h2{font-size:11px;font-weight:500;margin-bottom:7px}
.sum-body p{margin-bottom:3px}
.sum-sign{margin-top:10px}
.doc-h{position:absolute;top:218px;left:17px;font-size:8px;font-weight:700}
.doc-table{position:absolute;top:233px;left:17px;width:266px;border-collapse:collapse;font-size:4.5px;z-index:2}
.doc-table th{background:var(--brand);color:#fff;font-size:6.5px;font-weight:700;height:12px;padding:0 2px;border:1px solid #fff;white-space:nowrap}
.doc-table td{height:22px;border:1px solid var(--navy);text-align:left;padding-left:8px;background:rgba(255,255,255,.6)}
.doc-photo{position:absolute;top:270px;bottom:13px;left:0;right:0;background:linear-gradient(180deg,#fff 0%,#cfeef4 22%,#3ec6d4 50%,#0f6a90 75%,#07233f 100%)}

/* section bars */
.section-bar{display:inline-block;background:var(--navy);color:#fff;font-size:10px;font-weight:400;line-height:13px;padding:0 10px 0 18px;margin-left:-18px;clip-path:polygon(0 0,100% 0,96% 100%,0 100%);margin-top:4px}
.scope-body{position:absolute;top:48px;left:18px;right:14px;font-size:4.6px;line-height:1.4;z-index:2}
.scope-body p,.scope-body li{margin:3px 0 5px 3px}
.scope-body ul{list-style:none}
.scope-body li::before{content:"• "}
.scope-body li.b{font-weight:700}
.scope-deco{position:absolute;right:0;top:200px;bottom:13px;width:200px;background:linear-gradient(200deg,#fff 10%,#e3eef7 45%,#c5d9eb 70%,#f4f8fb)}

/* method */
.method-title{position:absolute;top:47px;left:17px;font-size:11px;font-weight:700}
.phase-band{position:absolute;top:64px;left:0;right:0;height:16px;background:var(--navy);display:flex;align-items:center;justify-content:space-around;padding:0 8px;color:#fff;font-size:7.5px;font-weight:700}
.phase-band svg{width:16px;height:8px}
.phase{position:absolute;display:flex;gap:6px;font-size:3.9px;line-height:1.35;color:#333;z-index:2}
.phase h3{font-size:7.5px;font-weight:700;color:var(--navy);min-width:36px;text-align:right;margin-top:10px}
.phase ol{padding-left:8px;width:85px}
.method-deco{position:absolute;left:0;right:0;top:290px;bottom:13px;background:linear-gradient(180deg,#fff 0%,#dbeef8 50%,#8fcbe8 85%,#cfe7f4)}
</style>
</head>
<body>

<!-- Cover -->
<section class="page p-cover">
  <div class="cover-logo"><div class="wordmark"><span class="dot"></span>dellvane</div></div>
  <div class="cover-photo" role="img" aria-label="Fotografia de um dedo a tocar num ecrã com dados luminosos em tons azuis e rosa"></div>
  <h1 class="cover-title">PROPOSTA ABC</h1>
  <div class="cover-client">Cliente</div>
  <div class="cover-date">10 de setembro de 2018</div>
  <div class="cover-ref">Ref : DLVxxxxxx</div>
  <div class="cover-band">www.dellvane-example.com</div>
</section>

<!-- Table of contents -->
<section class="page p-toc">
  <div class="toc-logo"><div class="wordmark"><span class="dot"></span>dellvane</div></div>
  <div class="blue-rule" style="top:60px"></div>
  <div class="toc-bg"></div>
  <h2 class="toc-title">Table of Contents</h2>
  <ul class="toc-list">
    <li class="lvl1">Proposta ABC<span class="leader"></span>1</li>
    <li>Sumário<span class="leader"></span>1</li>
    <li>Controlo de documento<span class="leader"></span>1</li>
    <li>Confidencialidade<span class="leader"></span>1</li>
    <li>Sumário executivo<span class="leader"></span>1</li>
    <li>Enquadramento<span class="leader"></span>1</li>
    <li>Proposta ABC<span class="leader"></span>1</li>
    <li>Sumário<span class="leader"></span>1</li>
    <li>Controlo de documento<span class="leader"></span>1</li>
    <li>Confidencialidade<span class="leader"></span>1</li>
    <li>Sumário executivo<span class="leader"></span>1</li>
    <li>Enquadramento<span class="leader"></span>1</li>
    <li>Âmbito<span class="leader"></span>1</li>
    <li class="lvl1">Definição<span class="leader"></span>1</li>
    <li>Solução Técnica<span class="leader"></span>1</li>
    <li>Solução técnica A<span class="leader"></span>1</li>
    <li>Arquitectura e componentes<span class="leader"></span>1</li>
    <li>Descrição funcional<span class="leader"></span>1</li>
    <li>Solução técnica B<span class="leader"></span>1</li>
    <li>Arquitectura e componentes<span class="leader"></span>1</li>
    <li>Descrição funcional<span class="leader"></span>1</li>
    <li>Proposta ABC<span class="leader"></span>1</li>
    <li class="lvl1">Sumário<span class="leader"></span>1</li>
    <li>Controlo de documento<span class="leader"></span>1</li>
    <li>Confidencialidade<span class="leader"></span>1</li>
    <li>Sumário executivo<span class="leader"></span>1</li>
    <li>Enquadramento<span class="leader"></span>1</li>
    <li>Âmbito<span class="leader"></span>1</li>
    <li class="lvl1">Definição<span class="leader"></span>1</li>
    <li>Solução Técnica<span class="leader"></span>1</li>
    <li>Solução técnica A<span class="leader"></span>1</li>
    <li>Arquitectura e componentes<span class="leader"></span>1</li>
    <li class="lvl1">Descrição funcional<span class="leader"></span>1</li>
    <li>Solução técnica B<span class="leader"></span>1</li>
    <li>Arquitectura e componentes<span class="leader"></span>1</li>
    <li>Descrição funcional<span class="leader"></span>1</li>
  </ul>
  <footer class="footer"><span>www.dellvane-example.com</span><span>2</span></footer>
</section>

<!-- Summary -->
<section class="page p-summary">
  <header class="inner-head">
    <div class="wordmark"><span class="dot"></span>dellvane</div>
    <address>Rua das Oliveiras nº 12 Parque Central – Bloco B – Piso 2<br>2600-100 Lisboa<br>Portugal<br>Tel +351210000000 | www.dellvane-example.com</address>
  </header>
  <div class="blue-rule"></div>
  <div class="doc-photo" role="img" aria-label="Fotografia de uma ponte suspensa sobre água com luz azul-turquesa"></div>
  <div class="sum-body">
    <h2>Sumário</h2>
    <p>Exmo. Dr./ Eng. &lt;pessoa que vai receber a proposta&gt;<br>&lt;Posição / cargo da pessoa na organização&gt;<br>No seguimento do pedido recebido, a Dellvane agradece a oportunidade de apresentar a sua proposta de colaboração profissional para apoiar &lt;nome do cliente&gt; no &lt;título da proposta&gt;.</p>
    <p>Ou</p>
    <p>A Dellvane agradece a oportunidade de apresentar a sua proposta ao desafio lançado pelo &lt;nome do cliente&gt; para responder ao Concurso Público Nº XXXXXXX para &lt;título da proposta&gt;.<br>Estamos, desde já, confiantes que a presente proposta vai ao encontro das vossas pretensões e expectativas, estando naturalmente ao vosso inteiro dispor para quaisquer esclarecimentos e/ou ajustamentos que julguem convenientes.<br>Reiteramos o nosso interesse e empenho em colaborar convosco.<br>Com os melhores cumprimentos,</p>
    <p class="sum-sign">Nome do account manager<br>Client Manager<br>Número movel<br>Endereço de email</p>
  </div>
  <h3 class="doc-h">Controlo de documento</h3>
  <table class="doc-table">
    <tr><th>Versão</th><th>Data</th><th>Autor</th><th>Comentários</th><th>Elaborado/modificado</th></tr>
    <tr><td>1.00</td><td></td><td></td><td>Original</td><td></td></tr>
    <tr><td></td><td></td><td></td><td></td><td></td></tr>
  </table>
  <footer class="footer"><span>www.dellvane-example.com</span><span>3</span></footer>
</section>

<!-- Scope -->
<section class="page p-scope">
  <header class="inner-head">
    <div class="wordmark"><span class="dot"></span>dellvane</div>
    <address>Rua das Oliveiras nº 12 Parque Central – Bloco B – Piso 2<br>2600-100 Lisboa<br>Portugal<br>Tel +351210000000 | www.dellvane-example.com</address>
  </header>
  <div class="blue-rule"></div>
  <div class="scope-deco" role="img" aria-label="Padrão abstrato de ondas suaves em cinza-azulado"></div>
  <div class="scope-body">
    <h2 class="section-bar">Testes</h2>
    <p>Engloba-se no âmbito destes serviços a realização de testes da solução, de forma a assegurar a qualidade global da mesma.</p>
    <h2 class="section-bar">Documentação</h2>
    <ul>
      <li>Requisitos Técnicos - Detalhe dos requisitos para cada parametrização da solução;</li>
      <li>Cronograma de Projeto - Plano detalhado do projeto;</li>
      <li>Relatório de Projeto - Documento final do projeto com a descrição da solução implementada;</li>
      <li>Auto de Receção - Documento final de aceitação da solução por parte do cliente.</li>
    </ul>
    <h2 class="section-bar">Prazos de Implementação</h2>
    <p>O início do projeto ocorrerá no mínimo <b>2 (duas) semanas</b> após a adjudicação. Após a reunião de kick-off do projeto será apresentado um cronograma detalhado.</p>
    <h2 class="section-bar">Exclusões</h2>
    <p>No âmbito dos serviços prestados estão excluídas as seguintes tarefas :</p>
    <ul>
      <li class="b">Lorem ipsum dolor sit</li>
      <li class="b">Lorem ipsum dolor sit amet</li>
      <li class="b">Lorem ipsum dolor sit ametconsectetur</li>
      <li class="b">Lorem ipsum dolor sit</li>
      <li class="b">Lorem ipsum dolor sit amet</li>
    </ul>
    <h2 class="section-bar">Formação</h2>
    <p>A concretização de ações de formação constitui um elemento fundamental para o sucesso da solução, uma vez que é através da formação que os colaboradores irão adquirir o conhecimento e experiência necessários à operacionalização da solução.</p>
    <p>Considerando as características da solução proposta, preconiza-se o seguinte plano de formação :</p>
    <ul>
      <li class="b">Lorem ipsum dolor sit</li>
      <li class="b">Lorem ipsum dolor sit amet</li>
      <li class="b">Lorem ipsum dolor sit ametconsectetur</li>
    </ul>
  </div>
  <footer class="footer"><span>www.dellvane-example.com</span><span>4</span></footer>
</section>

<!-- Method -->
<section class="page p-method">
  <header class="inner-head">
    <div class="wordmark"><span class="dot"></span>dellvane</div>
    <address>Rua das Oliveiras nº 12 Parque Central – Bloco B – Piso 2<br>2600-100 Lisboa<br>Portugal<br>Tel +351210000000 | www.dellvane-example.com</address>
  </header>
  <div class="blue-rule"></div>
  <div class="method-deco" role="img" aria-label="Malha geométrica abstrata de linhas e triângulos em azul claro"></div>
  <h2 class="method-title">Metodologia de gestão de projeto</h2>
  <div class="phase-band">
    <span>Iniciar</span><svg viewBox="0 0 16 8"><path d="M0 4h12M9 1l4 3-4 3" stroke="#249fd3" stroke-width="1.6" fill="none"/></svg>
    <span>Definir</span><svg viewBox="0 0 16 8"><path d="M0 4h12M9 1l4 3-4 3" stroke="#249fd3" stroke-width="1.6" fill="none"/></svg>
    <span>Construir</span><svg viewBox="0 0 16 8"><path d="M0 4h12M9 1l4 3-4 3" stroke="#249fd3" stroke-width="1.6" fill="none"/></svg>
    <span>Entregar</span><svg viewBox="0 0 16 8"><path d="M0 4h12M9 1l4 3-4 3" stroke="#249fd3" stroke-width="1.6" fill="none"/></svg>
    <span>Fechar</span>
  </div>
  <div class="phase" style="top:86px;left:0">
    <h3>Iniciar</h3>
    <ol><li>Analisar a alto nível a solução a implementar;</li><li>Coordenar as atividades relevantes do projeto:<br>• Gestão de âmbito;<br>• Gestão de recursos;<br>• Gestão de riscos.</li><li>Realizar reunião de início de projeto.</li></ol>
  </div>
  <div class="phase" style="top:86px;left:142px">
    <h3>Definir</h3>
    <ol><li>Levantar e validar requisitos;</li><li>Verificar condições no local (caso aplicável);</li><li>Elaborar plano detalhado.</li></ol>
  </div>
  <div class="phase" style="top:160px;left:0">
    <h3>Construir</h3>
    <ol><li>Elaborar desenho da solução e definir configurações;</li><li>Elaborar plano de testes;</li><li>Realizar testes de comissioning e staging dos equipamentos;</li><li>Expedir equipamentos para os locais de instalação.</li></ol>
  </div>
  <div class="phase" style="top:150px;left:148px">
    <h3>Entregar</h3>
    <ol><li>Instalar fisicamente os equipamentos;</li><li>Aplicar a configuração e testar os equipamentos;</li><li>Instalar fisicamente os terminais;</li><li>Ministrar formação na ótica do utilizador;</li><li>Elaborar plano de migração e roll-back;</li><li>Migrar para a nova solução;</li><li>Realizar testes de validação do funcionamento da nova solução;</li><li>Acompanhar a entrada em produção;</li><li>Efetuar sign-off da solução;</li><li>Elaborar documentação final de projeto.</li></ol>
  </div>
  <div class="phase" style="top:250px;left:0">
    <h3>Fechar</h3>
    <ol><li>Entregar documentação final de projeto;</li><li>Proceder à aceitação de fecho de projeto.</li></ol>
  </div>
  <footer class="footer"><span>www.dellvane-example.com</span><span>5</span></footer>
</section>

</body>
</html>
```